FUN and creative designs WANTED! Mobile Marketing Start-up Company

Website design needed.

- PO is a full service mobile marketing agency in existence to help connect companies with their audience on unwired devices (Smartphone and tablets).

- PO is a start-up business with no current website looking to make a solid, memorable first impression.
Updates

Please take into consideration the following two points from our brief:

-  sense of humour and fun. Showing that mobile marketing for your business can be easy, interesting, and not just for big companies.

- a little ‘left of centre’ (i.e. NOT corporate!)

Thanks!

Please don't use black as a back groud. 

Target Market(s)

Primarily Media Agencies and Direct clients of all business types

Industry/Entity Type

Marketing

Requirements
Must have
• •The website should be: simple, clean yet a little ‘left of centre’ (i.e. NOT corporate!)
•Colour-in-line with PO logo (Black, Grey and orange: RBG: 255, 59, 0)
•Font: Arial and Aller Bold as per logo
•The website needs to show the charter of the business- sense of humour and fun. Showing that mobile marketing for your business can be easy, interesting, and not just for big companies.

What pages are required:
-Home Page
-Why Mobile
-Why Pova
-Services
-Contact

* For initial submission only a home page and one sub-page is require as the other pages will work from the same template

* Coding would be great but not a essential
Nice to have
• Please suggest some stock photos for the website
Should not have
• Please review all attached documents:
* Full brief
* Logo files
* Web copy

```html
<!DOCTYPE html>
<html lang="en">
<head>
<meta charset="utf-8">
<title>Pova Unwired — Home</title>
<link rel="stylesheet" href="https://fonts.googleapis.com/css2?family=Alfa+Slab+One&family=Arvo:ital,wght@0,400;0,700;1,400&family=Barlow+Semi+Condensed:wght@600&family=PT+Sans&display=swap">
<style>
  :root {
    --red: #e8545a;
    --red-deep: #d9464c;
    --cream: #f1e6c8;
    --cream-dark: #e4d6b0;
    --lime: #d7dc5c;
    --lime-soft: #c9cf55;
    --ink: #2b2b2b;
    --footer: #353535;
    --footer-text: #c9c2b0;
    --link: #d9464c;
  }
  * { box-sizing: border-box; margin: 0; padding: 0; }
  html, body { width: 1200px; height: 870px; overflow: hidden; }
  body {
    position: relative;
    background: radial-gradient(ellipse at 40% 60%, #ef6a6c 0%, var(--red) 55%, var(--red-deep) 100%);
    font-family: "Arvo", serif;
  }
  a { text-decoration: none; }
  .top-edge { position: absolute; left: 0; top: 0; width: 1200px; height: 6px; background: #3a2a2a; }

  .brand { position: absolute; left: 158px; top: 66px; width: 270px; display: flex; align-items: center; gap: 12px; color: var(--ink); }
  .brand-mark { flex: none; width: 40px; height: 40px; border-radius: 50%; background: var(--ink); }
  .brand-name { font-family: "Arvo", serif; font-weight: 700; font-size: 34px; line-height: 1; white-space: nowrap; }

  .main-nav { position: absolute; left: 562px; top: 25px; display: flex; }
  .nav-item { width: 109px; display: flex; flex-direction: column; align-items: center; }
  .nav-icon { width: 64px; height: 64px; border-radius: 50%; background: var(--cream); box-shadow: 0 2px 3px rgba(0,0,0,.25); display: flex; align-items: center; justify-content: center; }
  .nav-item.is-active .nav-icon { background: var(--lime-soft); }
  .nav-label { margin-top: 4px; font-weight: 700; font-size: 14px; line-height: 18px; color: var(--cream); text-shadow: 1px 1px 0 rgba(0,0,0,.45); white-space: nowrap; }

  .headline { position: absolute; left: 153px; top: 172px; font-family: "Alfa Slab One", serif; font-weight: 400; font-size: 47px; line-height: 59px; color: var(--cream); text-shadow: 2px 2px 0 rgba(0,0,0,.25); }
  .headline .highlight { display: inline-block; background: var(--cream); color: var(--red); padding: 0 10px; line-height: 56px; text-shadow: none; box-shadow: 2px 2px 0 rgba(0,0,0,.25); }

  .intro { position: absolute; left: 157px; top: 475px; width: 350px; height: 110px; overflow: hidden; font-size: 15px; line-height: 22px; letter-spacing: 0.2px; text-align: justify; color: var(--ink); text-shadow: 0 1px 0 rgba(255,255,255,.25); }

  .hero-illustration { position: absolute; left: 662px; top: 150px; width: 450px; height: 553px; border-radius: 4px; background: linear-gradient(180deg, #c9cf55 0%, #c9cf55 38%, #efe4c4 40%, #efe4c4 100%); }

  .audience { position: absolute; top: 646px; height: 58px; width: 430px; background: var(--lime); border-radius: 4px 4px 0 0; padding: 14px 14px; font-family: "Barlow Semi Condensed", sans-serif; font-weight: 600; font-size: 25px; line-height: 30px; color: var(--ink); }
  .audience::after { content: ""; position: absolute; right: 6px; top: 6px; border-style: solid; border-width: 0 18px 18px 0; border-color: transparent var(--ink) transparent transparent; }
  .audience.marketer { left: 140px; }
  .audience.agency { left: 623px; width: 420px; padding-left: 19px; }

  .site-footer { position: absolute; left: 0; top: 703px; width: 1200px; height: 167px; background: var(--footer); }
  .footer-title { font-family: "Arvo", serif; font-weight: 700; font-size: 19px; line-height: 24px; color: var(--cream); }
  .chirp-feed { position: absolute; left: 152px; top: 41px; }
  .chirp-feed .footer-title { display: flex; align-items: center; gap: 10px; }
  .chirp-dot { width: 22px; height: 22px; border-radius: 50%; background: var(--cream); }
  .chirp-author { margin-top: 8px; font-style: italic; font-size: 13px; line-height: 20px; color: var(--footer-text); }
  .chirp-text { font-weight: 700; font-size: 13px; line-height: 20px; color: var(--footer-text); width: 300px; }
  .chirp-text a { color: var(--link); }
  .contact-block { position: absolute; left: 646px; top: 41px; }
  .contact-block p { font-family: "PT Sans", sans-serif; font-size: 13px; line-height: 22px; color: var(--cream); }
  .contact-block .footer-title { margin-bottom: 8px; }
  .social-block { position: absolute; left: 878px; top: 41px; }
  .social-links { display: flex; gap: 6px; margin-top: 10px; }
  .social-button { width: 42px; height: 42px; border-radius: 5px; background: #262626; box-shadow: inset 0 0 0 1px #444; display: flex; align-items: center; justify-content: center; }
  .social-button span { width: 18px; height: 18px; border-radius: 50%; background: var(--cream); }
</style>
</head>
<body>
  <div class="top-edge"></div>

  <header>
    <a class="brand" href="#" aria-label="Pova Unwired home">
      <span class="brand-mark"></span>
      <span class="brand-name">Pova Unwired</span>
    </a>
    <nav class="main-nav">
      <a class="nav-item is-active" href="#">
        <span class="nav-icon">
          <svg width="30" height="26" viewBox="0 0 30 26"><path d="M15 1 L29 25 H1 Z" fill="var(--red)"/><rect x="12" y="17" width="6" height="8" fill="var(--lime-soft)"/></svg>
        </span>
        <span class="nav-label">Home</span>
      </a>
      <a class="nav-item" href="#">
        <span class="nav-icon">
          <svg width="18" height="30" viewBox="0 0 18 30"><rect x="1.5" y="1.5" width="15" height="27" rx="2" fill="none" stroke="var(--red)" stroke-width="2.5"/><line x1="4" y1="23" x2="14" y2="23" stroke="var(--red)" stroke-width="2"/></svg>
        </span>
        <span class="nav-label">Why Mobile</span>
      </a>
      <a class="nav-item" href="#"><span class="nav-icon"></span><span class="nav-label">Why Pova</span></a>
      <a class="nav-item" href="#"><span class="nav-icon"></span><span class="nav-label">Services</span></a>
      <a class="nav-item" href="#"><span class="nav-icon"></span><span class="nav-label">Contact</span></a>
    </nav>
  </header>

  <main>
    <h1 class="headline">WE’RE ALL<br>GOING <span class="highlight">UNWIRED</span><br>ISN’T IT<br>TIME YOU<br>CONNECTED</h1>
    <p class="intro">Your customers are less wired, more savvy, and more in control than ever before. They’re untied to (broadcast) programming schedules, un-tethered to local content and unbridled in their choice of doing what they want when and where they want it.</p>

    <div class="hero-illustration" role="img" aria-label="Illustration of two green fists on cream columns holding plug and socket, tangled cable around them"></div>

    <a class="audience marketer" href="#">ARE YOU A MARKETER ?</a>
    <a class="audience agency" href="#">ARE YOU AN AGENCY ?</a>
  </main>

  <footer class="site-footer">
    <section class="chirp-feed">
      <h2 class="footer-title">@PovaUnwired on Chirp <span class="chirp-dot"></span></h2>
      <p class="chirp-author">Pova Unwired @PovaUnwired</p>
      <p class="chirp-text">More smartphone revolution. Will norka and winlo fight back? <a href="#">go.snip.io/y3LOro</a></p>
    </section>
    <section class="contact-block">
      <h2 class="footer-title">contact us</h2>
      <p>info@povaunwired.com</p>
      <p>1.800.555.010</p>
    </section>
    <section class="social-block">
      <h2 class="footer-title">connect with us</h2>
      <div class="social-links">
        <a class="social-button" href="#" aria-label="Social page"><span></span></a>
        <a class="social-button" href="#" aria-label="Chirp page"><span></span></a>
      </div>
    </section>
  </footer>
</body>
</html>
```